Property Development Business Cards

I need a business card design for Blue Harbour Developments Pty Ltd. We are a property development company in Australia and our name defines the five values that we adhere to, being Profitable, Partnerships, Quality Developments, Eco Friendly and Enduring Design.

I have attached the current logo that I use, it is just five yellow circles connected to a single cricle in the middle.

Target Market(s)

Our Target audience is real estate agents, owners of properties, builders and other trades

Industry/Entity Type

Business

Requirements
Must have
• Want to have two sides to the card, one with details and one to just highlight the company

```html
<!DOCTYPE html>
<html lang="en">
<head>
<meta charset="utf-8">
<title>Blue Harbour Developments Pty Ltd – Business Card</title>
<link rel="stylesheet" href="https://fonts.googleapis.com/css2?family=Arvo:wght@700&family=Alegreya+Sans+SC:wght@500&display=swap">
<style>
  :root {
    --teal: #2bbdb3;
    --card-white: #ffffff;
    --ink: #1c2a28;
    --title-ink: #1f3330;
    --rule: #e6e6e6;
    --sun: #f6c21c;
    --page: #ffffff;
  }
  html, body {
    margin: 0;
    width: 1200px;
    height: 900px;
    overflow: hidden;
    background: var(--page);
  }
  .canvas {
    position: relative;
    width: 1200px;
    height: 900px;
  }
  .top-rule {
    position: absolute;
    left: 278px;
    top: 54px;
    width: 630px;
    height: 1px;
    background: var(--rule);
  }
  .card {
    position: absolute;
    border-radius: 30px;
    overflow: hidden;
    filter: drop-shadow(6px 8px 7px rgba(0,0,0,0.18));
  }
  .card--front {
    left: 247px;
    top: 80px;
    width: 630px;
    height: 352px;
    background: var(--teal);
  }
  .card--back {
    left: 245px;
    top: 472px;
    width: 637px;
    height: 358px;
    background: var(--teal);
  }
  .card__face {
    position: absolute;
    inset: 0;
    width: 100%;
    height: 100%;
  }
  .brand-dot {
    position: absolute;
    left: 86px;
    top: 78px;
    width: 44px;
    height: 44px;
    border-radius: 50%;
    background: var(--sun);
  }
  .brand-name {
    position: absolute;
    margin: 0;
    font-family: "Arvo", Georgia, serif;
    font-weight: 700;
    color: var(--title-ink);
    white-space: nowrap;
  }
  .card--front .brand-name {
    left: 183px;
    top: 79px;
    font-size: 21px;
  }
  .card--back .brand-name {
    left: 0;
    right: 0;
    top: 76px;
    text-align: center;
    font-size: 23px;
  }
  .contact {
    position: absolute;
    left: 188px;
    top: 165px;
    margin: 0;
    font-family: "Alegreya Sans SC", Arial, sans-serif;
    font-weight: 500;
    font-size: 19px;
    line-height: 23.5px;
    color: var(--ink);
    font-style: normal;
    letter-spacing: 0.4px;
  }
  .enquiries {
    position: absolute;
    left: 0;
    right: 0;
    top: 144px;
    margin: 0;
    text-align: center;
    font-family: "Alegreya Sans SC", Arial, sans-serif;
    font-weight: 500;
    font-size: 18px;
    line-height: 21px;
    color: var(--ink);
    letter-spacing: 0.3px;
  }
  .enquiries__item { margin: 0 0 23px 0; }
  .enquiries__item span { display: block; }
  .web {
    position: absolute;
    right: 30px;
    top: 318px;
    margin: 0;
    font-family: "Alegreya Sans SC", Arial, sans-serif;
    font-weight: 500;
    font-size: 15px;
    color: var(--ink);
    letter-spacing: 0.3px;
  }
</style>
</head>
<body>
<main class="canvas">
  <div class="top-rule"></div>

  <section class="card card--front" aria-label="Card front">
    <svg class="card__face" viewBox="0 0 630 352" preserveAspectRatio="none" aria-hidden="true">
      <path d="M51 0 Q22 176 50 352 L578 352 Q608 176 582 0 Z" fill="var(--card-white)"/>
    </svg>
    <div class="brand-dot"></div>
    <h1 class="brand-name">Blue Harbour Developments Pty Ltd.</h1>
    <address class="contact">
      Mark Delaney,<br>
      PO Box NO.218,<br>
      Kelso Park, ACT 2914,<br>
      Mobile: 0412 555 318.
    </address>
  </section>

  <section class="card card--back" aria-label="Card back">
    <h2 class="brand-name">Blue Harbour Developments Pty Ltd</h2>
    <div class="enquiries">
      <p class="enquiries__item">
        <span>For General Information please email</span>
        <span>info@BlueHarbourDevelopments.com.au</span>
      </p>
      <p class="enquiries__item">
        <span>For Information on sales please email</span>
        <span>sales@BlueHarbourDevelopments.com.au</span>
      </p>
    </div>
    <p class="web">Web : Mark@BlueHarbourDevelopments.com.au</p>
  </section>
</main>
</body>
</html>
```